Talents and colours poster for home office

The objective is to illustrate/communicate and remember 5 talents and 4 colours of the personality.

The infographic will be hanged on the wall of an home office. It need to be simple and clear. Illustrations and pictograms can be used. It can be artistic.

Here's the content:

5 talents,scaling in priority from #1 to #5
Ideation / creativity
Winning other over / charisma
Adaptability
Positivity
Empathy

In the files there is a description of what those mean.

You have to include 4 colours, scaling in priority from #1 to #4
Yellow
Green
Red
Blue

I made a sketch just for fun... and to show why I need professionnal skills :)

THX

Industry/Entity Type

Office

Requirements
Should not have
• offensive materials

```html
<!DOCTYPE html>
<html lang="en">
<head>
<meta charset="utf-8">
<title>Talents and Colours Poster</title>
<link href="https://fonts.googleapis.com/css2?family=Oswald:wght@500;600&display=swap" rel="stylesheet">
<style>
  :root {
    --frame-dark: #2a0f0c;
    --frame-mid: #5a2118;
    --frame-light: #8a3a2a;
    --wood-light: #e6b27a;
    --wood-deep: #c98d52;
    --mat-outer: #5f564c;
    --mat: #7a7063;
    --gold: #e2b84c;
    --gold-light: #f6dc8a;
    --board: #221e1c;
    --edge-dark: #1c1917;
    --edge-rim: #3a3532;
    --yellow: #f7e62a;
    --green: #8bbb3f;
    --red: #e22f28;
    --blue: #344a8a;
    --light-blue: #6f93c6;
    --ink-dark: #231f20;
    --ink-light: #ffffff;
  }
  * { margin: 0; padding: 0; box-sizing: border-box; }
  html, body { width: 929px; height: 1200px; overflow: hidden; }
  body { position: relative; background: var(--frame-dark); font-family: 'Oswald', sans-serif; }

  .frame {
    position: absolute; inset: 0;
    background: var(--frame-dark);
    box-shadow:
      inset 0 0 0 10px var(--frame-mid),
      inset 0 0 0 14px var(--frame-dark),
      inset 0 0 0 30px var(--frame-mid),
      inset 0 0 0 34px var(--frame-light),
      inset 0 0 0 52px var(--frame-dark),
      inset 0 0 0 58px var(--frame-mid),
      inset 0 0 0 78px var(--frame-dark),
      inset 0 0 0 84px var(--frame-light);
  }
  .frame-mitres { position: absolute; inset: 0; }

  .mat {
    position: absolute; left: 90px; top: 73px; width: 749px; height: 1052px;
    background: var(--mat);
    box-shadow: inset 0 0 0 12px var(--mat-outer);
  }
  .gold-border {
    position: absolute; left: 146px; top: 120px; width: 637px; height: 955px;
    border: 10px solid var(--gold);
    box-shadow: inset 0 0 0 2px var(--gold-light), 0 0 0 2px var(--gold-light);
    background: var(--board);
  }

  .band {
    position: absolute; left: 193px; width: 546px;
    display: flex; align-items: center; justify-content: center;
    font-weight: 600; font-size: 35px; letter-spacing: -0.3px;
    text-transform: uppercase; white-space: nowrap;
  }
  .band--ideation { top: 214px; height: 132px; background: var(--yellow); color: var(--ink-dark); }
  .band--charisma { top: 370px; height: 136px; background: var(--green); color: var(--ink-dark); }
  .band--adaptability { top: 530px; height: 136px; background: var(--red); color: var(--ink-light); }
  .band--positivity { top: 690px; height: 138px; background: var(--blue); color: var(--ink-light); }
  .band--empathy { top: 852px; height: 136px; background: var(--light-blue); color: var(--ink-light); }

  .band-edge {
    position: absolute; left: 193px; width: 546px; height: 24px;
    background: linear-gradient(180deg, var(--edge-rim), var(--edge-dark) 50%, var(--edge-rim));
  }
  .band-edge--top { top: 200px; height: 14px; }
  .band-edge--bottom { top: 988px; height: 14px; }

  .corner-piece { position: absolute; width: 150px; height: 122px; }
  .corner-piece--tl { left: 0; top: 0; clip-path: polygon(0 0, 100% 0, 0 100%); background: linear-gradient(135deg, var(--wood-light), var(--wood-deep)); }
  .corner-piece--tr { right: 0; top: 0; clip-path: polygon(0 0, 100% 0, 100% 100%); background: linear-gradient(225deg, var(--wood-light), var(--wood-deep)); }
  .corner-piece--bl { left: 0; bottom: 0; clip-path: polygon(0 0, 100% 100%, 0 100%); background: linear-gradient(45deg, var(--wood-light), var(--wood-deep)); }
  .corner-piece--br { right: 0; bottom: 0; clip-path: polygon(100% 0, 100% 100%, 0 100%); background: linear-gradient(315deg, var(--wood-light), var(--wood-deep)); }
</style>
</head>
<body>
  <div class="frame"></div>
  <svg class="frame-mitres" width="929" height="1200" viewBox="0 0 929 1200">
    <g stroke="#120605" stroke-width="2">
      <line x1="0" y1="0" x2="90" y2="73"/>
      <line x1="929" y1="0" x2="839" y2="73"/>
      <line x1="0" y1="1200" x2="90" y2="1125"/>
      <line x1="929" y1="1200" x2="839" y2="1125"/>
    </g>
  </svg>

  <div class="mat"></div>
  <div class="gold-border"></div>

  <div class="band band--ideation">Ideation / Creativity</div>
  <div class="band band--charisma">Winning Other Over / Charisma</div>
  <div class="band band--adaptability">Adaptability</div>
  <div class="band band--positivity">Positivity</div>
  <div class="band band--empathy">Empathy</div>

  <div class="band-edge band-edge--top" role="img" aria-label="Decorative scalloped edge"></div>
  <div class="band-edge" style="top:346px" role="img" aria-label="Decorative scalloped divider"></div>
  <div class="band-edge" style="top:506px" role="img" aria-label="Decorative scalloped divider"></div>
  <div class="band-edge" style="top:666px" role="img" aria-label="Decorative scalloped divider"></div>
  <div class="band-edge" style="top:828px" role="img" aria-label="Decorative scalloped divider"></div>
  <div class="band-edge band-edge--bottom" role="img" aria-label="Decorative scalloped edge"></div>

  <div class="corner-piece corner-piece--tl" role="img" aria-label="Wooden corner piece"></div>
  <div class="corner-piece corner-piece--tr" role="img" aria-label="Wooden corner piece"></div>
  <div class="corner-piece corner-piece--bl" role="img" aria-label="Wooden corner piece"></div>
  <div class="corner-piece corner-piece--br" role="img" aria-label="Wooden corner piece"></div>
</body>
</html>
```